Companybrochure for Consulting & Financing Firm

I need to have a Company Brochure asap for our company. We have a website that describes what we do, but we need also a brochure, that can be sent by PDF of eventually be printed as well.

The brochure should be short but nice and appealing to the customers.

We provide professional management consulting and help our customers to get finance for very diferent projects. Our business has a lot to do with personal relations, but also we are very professional in the way we work and how develop the solutions for our clients. Our clients are mainly government-owned firm, but also private trading companies and wealthy private investors.

Our customers are mainly in Latin America, but the company is headquater is in Switzerland. We are opening offices in Panama and Caracas, this should be easaly be adabtable later.

Please have a look at our website www.valtorhaus.ch. In the brochure, we would segment our services in 1.) Project Developments 2.) Management Conulting 3.) Investment Management and 4.) Finance Solutions.

Also do have a look at www.valtorhaus.ch
(Click E for the English version)
Updates

I managed to put the Mock-Up to the Website.
It is actually not really a mock-up, it is a version I have designed myself.
Well as I am not a designer, I hope you can make it much better.
The content however is what I would put in any other design as well.

Target Market(s)

Top Management, Investors, Entrepreneurs, Government Officials

Industry/Entity Type

Management Consulting

Requirements
Must have
• Design should reflect this image elements:

We are entrepreneurs.
We are comitted to get things done.
We work closely with the client side by side.
We are a professional partner.
We are not afraid of delivering unconventional solutions.
We look at the problem from various angles.
We analyse, develop solutions and implent results.
Should not have
• Typical US-American style elements. We do not want to give the impression of being a US company.

We do not want to appear to be neo-liberal. We are a politically neutral professional consulting firm.

```html
<!DOCTYPE html>
<html lang="en">
<head>
<meta charset="utf-8">
<title>Valtorhaus – Company Brochure</title>
<link rel="stylesheet" href="https://fonts.googleapis.com/css2?family=Open+Sans:wght@400;600;700&display=swap">
<style>
  :root {
    --bg: #f3f3f1;
    --paper: #ffffff;
    --ink: #333a44;
    --brand-blue: #3b66a6;
    --deep-blue: #1f4f92;
    --green: #6b9a2c;
    --orange: #b0690f;
    --navy: #1d4c78;
    --purple: #9a4ea6;
    --rule: #d9dde3;
  }
  * { box-sizing: border-box; margin: 0; padding: 0; }
  html, body { width: 1200px; height: 900px; overflow: hidden; }
  body {
    background: var(--bg);
    font-family: "Open Sans", Arial, sans-serif;
    color: var(--ink);
    position: relative;
  }
  .page {
    position: absolute;
    width: 170px;
    height: 240px;
    background: var(--paper);
    overflow: hidden;
    box-shadow: 0 2px 8px rgba(0,0,0,.12);
  }
  .spread { position: absolute; width: 340px; height: 240px; box-shadow: 0 2px 8px rgba(0,0,0,.12); }
  .spread .page { box-shadow: none; top: 0; }
  .spread .page.left { left: 0; }
  .spread .page.right { left: 170px; border-left: 1px solid #eceef1; }

  .photo { position: absolute; }

  /* Cover */
  .cover { left: 260px; top: 210px; }
  .cover .brand-name {
    position: absolute; right: 10px; top: 22px;
    font-size: 13px; font-weight: 700; color: #111;
  }
  .cover .motto-band {
    position: absolute; left: 0; right: 0; top: 44px; height: 12px;
    background: var(--deep-blue); color: #fff;
    font-size: 5px; font-weight: 600; letter-spacing: 1px;
    text-align: right; padding-right: 10px; line-height: 12px;
  }
  .cover .photo {
    left: 0; right: 0; top: 56px; bottom: 0;
    background: linear-gradient(180deg, #e9eef3 0%, #5f96cf 22%, #2f6ea8 48%, #dfe3e6 62%, #f4f4f2 100%);
  }

  /* Back cover */
  .back-cover { left: 260px; top: 500px; }
  .back-cover .field {
    position: absolute; left: 0; right: 0; top: 42px; bottom: 0;
    background: var(--brand-blue);
    color: #e6edf7; padding: 0 12px;
  }
  .back-cover .contact { position: absolute; left: 12px; top: 118px; font-size: 3.6px; line-height: 5.5px; }
  .back-cover .statement { position: absolute; left: 12px; top: 160px; width: 120px; font-size: 4px; line-height: 6px; letter-spacing: .3px; }

  /* Spread shared */
  .header-band {
    position: absolute; left: 0; right: 0; top: 10px; height: 26px;
    color: #fff; font-size: 6px; font-weight: 700; letter-spacing: .6px;
    padding: 7px 12px; line-height: 7px;
  }
  .subhead { position: absolute; left: 12px; top: 44px; width: 100px; font-size: 3.6px; font-weight: 600; line-height: 5px; letter-spacing: .2px; }
  .body-copy { position: absolute; left: 12px; top: 70px; width: 100px; font-size: 3.2px; line-height: 4.6px; color: #555; }
  .side-box {
    position: absolute; right: 10px; top: 44px; width: 40px; height: 70px;
    color: #fff; font-size: 3.2px; line-height: 4.6px; padding: 5px;
  }
  .side-box b { display: block; font-weight: 700; margin-bottom: 3px; }
  .spread .photo { left: 0; right: 0; top: 125px; bottom: 0; }

  /* Spread 1 */
  .spread-intro { left: 590px; top: 30px; }
  .spread-intro .photo-full {
    position: absolute; inset: 0;
    background: linear-gradient(150deg, #6f93c6 0%, #9fb9dc 40%, #c9d8ea 60%, #5f88c0 100%);
  }
  .spread-intro .statements {
    position: absolute; left: 200px; top: 18px; width: 120px;
    display: flex; gap: 10px; color: #fff; font-size: 3.4px; line-height: 4.8px;
  }
  .spread-intro .statements b { display: block; font-weight: 700; margin-bottom: 3px; }
  .spread-intro .motto-box {
    position: absolute; right: 12px; bottom: 18px; width: 52px; height: 30px;
    background: var(--deep-blue); color: #fff;
    font-size: 5px; font-weight: 700; letter-spacing: .8px; line-height: 6.5px; padding: 5px 6px;
  }

  /* Spread 2 */
  .spread-services-a { left: 590px; top: 330px; }
  .green-band { background: var(--green); }
  .green-text { color: var(--green); }
  .green-box { background: #8db05a; }
  .orange-band { background: var(--orange); }
  .orange-text { color: var(--orange); }
  .orange-box { background: #c98e3e; }
  .process { position: absolute; left: 12px; top: 98px; display: flex; align-items: center; gap: 2px; }
  .process span {
    background: var(--orange); color: #fff; font-size: 3px; font-weight: 700;
    padding: 2px 4px; letter-spacing: .3px;
  }
  .process svg { width: 8px; height: 5px; }
  .photo.test-tubes { background: linear-gradient(160deg, #3f7d1f 0%, #9bcf6a 45%, #d7e8c3 70%, #5a8f2f 100%); }
  .photo.dome { background: linear-gradient(170deg, #d9dde0 0%, #a88457 45%, #6e4e2a 70%, #cfd6dc 100%); }

  /* Spread 3 */
  .spread-services-b { left: 590px; top: 620px; }
  .navy-band { background: var(--navy); }
  .navy-text { color: var(--navy); }
  .blue-box { background: #4f86bf; }
  .purple-band { background: var(--purple); }
  .purple-text { color: var(--purple); }
  .purple-box { background: #b783bf; }
  .photo.runner { background: linear-gradient(160deg, #16355f 0%, #3c6f9f 45%, #8eaecb 70%, #1f3f66 100%); }
  .photo.wind-field { background: linear-gradient(180deg, #c9a4c7 0%, #e8b6b3 40%, #7a8a5a 70%, #3f6b2a 100%); }
</style>
</head>
<body>

  <!-- Cover -->
  <section class="page cover">
    <div class="brand-name">Valtorhaus</div>
    <div class="motto-band">ANALYZE · DEVELOP · DELIVER</div>
    <div class="photo" role="img" aria-label="Photo of a white terrace with a view over a blue sea and sky"></div>
  </section>

  <!-- Back cover -->
  <section class="page back-cover">
    <div class="field">
      <div class="contact">
        Valtorhaus AG<br>
        Bahnhofstrasse 10<br>
        8001 Zurich<br>
        T +41 44 210 00 00<br><br>
        www.valtorhaus.ch
      </div>
      <p class="statement">VALTORHAUS AG IS AN INDEPENDENT FIRM IN A SWISS STOCK CORPORATION, SINCE 1996.</p>
    </div>
  </section>

  <!-- Spread 1: intro -->
  <section class="spread spread-intro">
    <div class="photo-full" role="img" aria-label="Photo of a dandelion seed head blowing against a blue sky"></div>
    <div class="statements">
      <div>
        <b>WE ARE A PROFESSIONAL CONSULTING PARTNER WORKING SIDE BY SIDE</b>
        We are entrepreneurs.<br>We are committed to get things done.
      </div>
      <div>
        <b>WE ARE ENTREPRENEURS</b>
        We look at problems from various angles.<br>We deliver unconventional solutions.
      </div>
    </div>
    <div class="motto-box">ANALYZE<br>DEVELOP<br>DELIVER</div>
  </section>

  <!-- Spread 2: project development / management consulting -->
  <section class="spread spread-services-a">
    <article class="page left">
      <h2 class="header-band green-band">PROJECT<br>DEVELOPMENT</h2>
      <p class="subhead green-text">WE DEVELOP PROJECTS FROM FIRST IDEA TO SOUND FINANCING AND LASTING RESULTS</p>
      <p class="body-copy">Our team structures public and private projects across Latin America with care and precision.<br><br>We work closely with every client.</p>
      <aside class="side-box green-box">We analyse, plan and follow each step with you.</aside>
      <div class="photo test-tubes" role="img" aria-label="Photo of glass test tubes in green light"></div>
    </article>
    <article class="page right">
      <h2 class="header-band orange-band">MANAGEMENT<br>CONSULTING</h2>
      <p class="subhead orange-text">WE SUPPORT MANAGEMENT TEAMS WITH CLEAR STRATEGY AND PRACTICAL SOLUTIONS</p>
      <p class="body-copy">From analysis to implementation we stay at your side until the results are delivered.</p>
      <div class="process">
        <span>ANALYZE</span>
        <svg viewBox="0 0 8 5"><path d="M0 2.5h6M4.5 1l2 1.5-2 1.5" fill="none" stroke="#b0690f" stroke-width=".8"/></svg>
        <span>DEVELOP</span>
        <svg viewBox="0 0 8 5"><path d="M0 2.5h6M4.5 1l2 1.5-2 1.5" fill="none" stroke="#b0690f" stroke-width=".8"/></svg>
        <span>DELIVER</span>
      </div>
      <aside class="side-box orange-box"><b>WHAT YOU CAN EXPECT FROM US</b>Direct access, discretion and reliable results.</aside>
      <div class="photo dome" role="img" aria-label="Photo of a geometric glass dome structure seen from below"></div>
    </article>
  </section>

  <!-- Spread 3: investment management / finance solutions -->
  <section class="spread spread-services-b">
    <article class="page left">
      <h2 class="header-band navy-band">INVESTMENT<br>MANAGEMENT</h2>
      <p class="subhead navy-text">WE MANAGE INVESTMENTS WITH A LONG-TERM VIEW AND CAREFUL JUDGEMENT</p>
      <p class="body-copy">Private investors and institutions trust us to protect and grow their assets.</p>
      <aside class="side-box blue-box">Independent advice, neutral and transparent.</aside>
      <div class="photo runner" role="img" aria-label="Photo of a runner in front of a modern glass building"></div>
    </article>
    <article class="page right">
      <h2 class="header-band purple-band">FINANCE<br>SOLUTIONS</h2>
      <p class="subhead purple-text">WE FIND THE RIGHT FINANCING FOR PROJECTS OF EVERY SIZE AND SECTOR</p>
      <p class="body-copy">Banks, funds and partners in Europe and Latin America form our network.</p>
      <aside class="side-box purple-box"><b>WHAT YOU CAN EXPECT FROM US</b>Tailored structures and fast decisions.</aside>
      <div class="photo wind-field" role="img" aria-label="Photo of wind turbines on a green field at dusk"></div>
    </article>
  </section>

</body>
</html>
```